Creative Brief
Marketing Collateral for Real Estate Business
Create matching postcards and Business Card.
MARKETING COLLATERAL FOR REAL ESTATE COMPANY
Create matching postcards, HTML email template and Business Card.
Postcard (5.5” x 8.5”) template
Email HTML template
Business Card
DESCRIPTION
Our office needs 2-3 “Just Listed” postcard templates for REAL ESTATE FORECLOSURE LISITNGS. The templates must display two logos which are provided (FindMarlowHomesteads.example to be large in size). We need the ability to insert pictures of each new listing inside within the template. The design must be colorful (earth tone colors), professional, simple and eye catching. Postcard: We also want 1-2 generic postcard templates where a standard/general real estate picture is already inserted which can be used for multiple/different properties.
Postcard templates must meet the printing specifications for PressNook.example. The templates must be provided in digital formats that are editable by the project holder. They must also be provided in print ready formats. Our company is based in Marlow, SC, USA. Please view images of Marlow, SC, USA via google if necessary for the postcard template.
The HTML Email Template(s) will be used to mass email our database with new listings.
Real Estate
Buyers of Real Estate Foreclosed Properties; Real Estate Investors.
DESIGN
POSTCARD COMMENTS / STATEMENTS TO BE INCLUDED WITHIN THE POSTCARD / EMAIL HTML
-PRE-LISTING(1-2 Templates)
-JUST LISTED (1-2 Templates)
-SEARCH HUNDREDS OF BANK OWNED FORECLOSURES – SIGN UP FREE! FINDMARLOWHOMESTEADS.EXAMPLE
-Join FindMarlowHomesteads.example and be the first to know about newly listed Marlow Foreclosures.
-Don’t miss this opportunity to buy a bank owned foreclosure.
-We are your Marlow Foreclosure Specialist!
-NEW LISTING ALERT – Sign up and receive listings meeting your criteria today! (in a highlighted icon or box or similar)
-This property is NOT listed in MLS yet. Please contact me if you are interested in purchasing this property. (disclaimer/small font))
POSTCARD SIZE
Postcard 5.5” x 8.5”
COLORS
Blue / Green / Tan (Earth tone colors) / To match FindMarlowHomesteads.example logo
Color (front and back)
Images and Date to be used

```html
<!DOCTYPE html>
<html lang="en">
<head>
<meta charset="utf-8">
<title>FindMarlowHomesteads – Postcard, Business Card and Email Signature Set</title>
<link href="https://fonts.googleapis.com/css2?family=Open+Sans:wght@400;600;700;800&family=Merriweather:wght@700&display=swap" rel="stylesheet">
<style>
  :root{
    --board:#8a6a4c;
    --paper:#ffffff;
    --blue:#1b4f8f;
    --blue-dark:#123a6b;
    --green:#7cb342;
    --green-dark:#4e8a2a;
    --tan:#d9c6a2;
    --ink:#2d2d2d;
    --muted:#6b6b6b;
    --label:#ffffff;
  }
  *{box-sizing:border-box;margin:0;padding:0}
  html,body{width:1200px;height:526px;overflow:hidden}
  body{background:var(--board);font-family:"Open Sans",Arial,sans-serif;color:var(--ink);position:relative}

  .board-title{position:absolute;top:6px;left:0;width:1200px;text-align:center;font-family:"Merriweather",Georgia,serif;font-size:24px;line-height:30px;color:var(--label);letter-spacing:.5px}
  .piece-label{position:absolute;font-size:11px;line-height:14px;font-weight:700;color:var(--label);white-space:nowrap}

  .piece{position:absolute;background:var(--paper);overflow:hidden;box-shadow:0 2px 6px rgba(0,0,0,.35)}
  .photo{position:absolute}

  /* brand lockup */
  .brand{position:absolute;display:flex;align-items:center;gap:3px;font-weight:700;color:var(--blue);white-space:nowrap}
  .brand .dot{border-radius:50%;background:var(--green);flex:none}

  /* postcard front */
  .front{width:192px;height:203px}
  .front .house{left:86px;top:0;width:106px;height:96px;background:linear-gradient(180deg,#a9c7e4 0%,#c9d6c0 55%,#6f8f4e 100%)}
  .front .agent{left:114px;top:70px;width:78px;height:112px;background:linear-gradient(180deg,#4a3d3a 0%,#2b2b33 100%)}
  .front .brand{left:8px;top:10px;font-size:8px}
  .front .brand .dot{width:12px;height:12px}
  .front .search{position:absolute;left:10px;top:58px;font-size:11px;font-weight:800;color:var(--blue)}
  .front .hundreds{position:absolute;left:9px;top:72px;font-size:16px;font-weight:800;color:var(--green-dark);line-height:1;letter-spacing:-.2px}
  .front .partner{position:absolute;left:10px;top:100px;display:flex;align-items:center;gap:3px;font-size:6px;font-weight:700;color:var(--blue-dark)}
  .front .partner i{width:8px;height:8px;background:var(--tan);display:block}
  .front .teaser{position:absolute;left:0;top:140px;width:108px;height:28px;background:var(--blue);color:#fff;font-size:6.5px;font-weight:600;line-height:1.25;padding:4px 6px}
  .front .footer{position:absolute;left:0;bottom:0;width:192px;height:21px;background:var(--green);color:#fff;font-size:6.8px;font-weight:700;padding:6px 6px;white-space:nowrap}
  .front .swoosh{position:absolute;left:0;top:118px}

  /* postcard back */
  .back{width:274px;height:203px}
  .back .brand{left:8px;top:8px;font-size:8px}
  .back .brand .dot{width:12px;height:12px}
  .back .stamp{position:absolute;right:8px;top:8px;width:22px;height:26px;border:1px dashed var(--muted)}
  .back .mailing{position:absolute;left:168px;top:54px;font-size:6px;line-height:1.5;color:var(--ink)}
  .back .listing-main{left:8px;top:30px;width:70px;height:50px;background:linear-gradient(180deg,#b9d3ea,#8fa873)}
  .back .listing-a{left:82px;top:30px;width:34px;height:24px;background:linear-gradient(180deg,#c3d8ea,#97ac7b)}
  .back .listing-b{left:82px;top:56px;width:34px;height:24px;background:linear-gradient(180deg,#c3d8ea,#a2936f)}
  .back .headline{position:absolute;left:8px;top:86px;font-size:9px;font-weight:800;color:var(--blue);line-height:1.1}
  .back .headline b{color:var(--green-dark)}
  .back .agent{left:122px;top:84px;width:30px;height:42px;background:linear-gradient(180deg,#4a3d3a,#2b2b33)}
  .back .alert{position:absolute;left:8px;top:112px;width:92px;padding:3px 4px;background:var(--green);color:#fff;font-size:5.5px;font-weight:700;line-height:1.25}
  .back .disclaimer{position:absolute;left:8px;top:136px;width:140px;font-size:4.5px;color:var(--muted);line-height:1.3}
  .back .site{position:absolute;left:150px;top:150px;width:124px;height:14px;background:var(--blue);color:#fff;font-size:5.5px;font-weight:700;text-align:center;padding-top:3px}
  .back .icons{position:absolute;left:256px;top:104px;display:flex;flex-direction:column;gap:3px}
  .back .icons i{width:10px;height:10px;background:var(--blue);display:block;border-radius:2px}
  .back .wave{position:absolute;left:0;bottom:0}

  /* business card front */
  .bcard{width:115px;height:53px}
  .bcard .brand{left:6px;top:8px;font-size:7px}
  .bcard .brand .dot{width:10px;height:10px}
  .bcard .details{position:absolute;right:6px;top:6px;text-align:right;font-size:4.5px;line-height:1.35;color:var(--ink)}
  .bcard .details strong{font-size:5.5px;color:var(--blue)}
  .bcard .wave{position:absolute;left:0;bottom:0}

  /* business card back */
  .bcard-back{width:127px;height:66px}
  .bcard-back .brand{left:50%;top:26px;transform:translateX(-50%);font-size:7.5px}
  .bcard-back .brand .dot{width:10px;height:10px}
  .bcard-back .wave{position:absolute;left:0;bottom:0}
  .bcard-back.green{background:var(--green)}
  .bcard-back.green .brand{color:#fff}
  .bcard-back.green .brand .dot{background:#fff}

  /* email signature */
  .signature{width:160px;height:44px}
  .signature .brand{left:6px;top:9px;font-size:6.5px}
  .signature .brand .dot{width:9px;height:9px}
  .signature .details{position:absolute;left:80px;top:6px;font-size:4.5px;line-height:1.35}
  .signature .details strong{font-size:5.5px;color:var(--blue)}
  .signature .wave{position:absolute;left:0;bottom:0}
</style>
</head>
<body>

<h1 class="board-title">Post Card</h1>

<!-- ROW 1 -->
<span class="piece-label" style="left:16px;top:28px">Front</span>
<section class="piece front" style="left:12px;top:42px">
  <div class="photo house" role="img" aria-label="Photo of a Marlow home exterior"></div>
  <div class="brand"><span class="dot"></span>FindMarlowHomesteads</div>
  <svg class="swoosh" width="192" height="30" viewBox="0 0 192 30" aria-hidden="true"><path d="M0 22 Q70 2 192 14 L192 30 L0 30Z" fill="#7cb342" opacity=".35"/></svg>
  <div class="photo agent" role="img" aria-label="Portrait of the listing agent"></div>
  <p class="search">SEARCH</p>
  <p class="hundreds">HUNDREDS</p>
  <p class="partner"><i></i>Harlan Realty</p>
  <p class="teaser">A new foreclosure listing in your area will be listed soon!</p>
  <p class="footer">Join FindMarlowHomesteads.example to learn more.</p>
</section>

<span class="piece-label" style="left:214px;top:28px">Back</span>
<section class="piece back" style="left:211px;top:42px">
  <div class="brand"><span class="dot"></span>FindMarlowHomesteads</div>
  <div class="stamp"></div>
  <div class="photo listing-main" role="img" aria-label="Main listing photo"></div>
  <div class="photo listing-a" role="img" aria-label="Listing interior photo"></div>
  <div class="photo listing-b" role="img" aria-label="Listing yard photo"></div>
  <p class="mailing">Resident Name<br>12 Harbor Lane<br>Marlow, SC 29400</p>
  <p class="headline">DON'T MISS THIS<br><b>OPPORTUNITY!</b></p>
  <div class="photo agent" role="img" aria-label="Agent portrait"></div>
  <p class="alert">NEW LISTING ALERT – Sign up and receive listings today!</p>
  <p class="disclaimer">This property is NOT listed in MLS yet. Please contact me if you are interested in purchasing this property.</p>
  <div class="icons"><i></i><i></i><i></i></div>
  <p class="site">www.FindMarlowHomesteads.example</p>
  <svg class="wave" width="274" height="40" viewBox="0 0 274 40" aria-hidden="true"><path d="M0 26 Q120 6 274 24 L274 40 L0 40Z" fill="#7cb342"/><path d="M0 32 Q140 16 274 32 L274 40 L0 40Z" fill="#1b4f8f"/></svg>
</section>

<span class="piece-label" style="left:752px;top:78px">Business Card Front</span>
<section class="piece bcard" style="left:749px;top:96px">
  <div class="brand"><span class="dot"></span>FindMarlow</div>
  <p class="details"><strong>Agent Name</strong><br>Foreclosure Specialist<br>555-0142</p>
  <svg class="wave" width="115" height="20" viewBox="0 0 115 20" aria-hidden="true"><path d="M0 11 Q58 0 115 9 L115 20 L0 20Z" fill="#7cb342"/><path d="M0 15 Q58 7 115 14 L115 20 L0 20Z" fill="#1b4f8f"/></svg>
</section>

<span class="piece-label" style="left:850px;top:184px">Business Card Back</span>
<section class="piece bcard-back" style="left:845px;top:202px">
  <div class="brand"><span class="dot"></span>FindMarlow</div>
  <svg class="wave" width="127" height="18" viewBox="0 0 127 18" aria-hidden="true"><path d="M0 9 Q64 0 127 9 L127 18 L0 18Z" fill="#1b4f8f"/></svg>
</section>

<span class="piece-label" style="left:1020px;top:140px">Email Signature</span>
<section class="piece signature" style="left:1003px;top:157px">
  <div class="brand"><span class="dot"></span>FindMarlow</div>
  <p class="details"><strong>Agent Name</strong><br>Foreclosure Specialist<br>555-0142</p>
  <svg class="wave" width="160" height="10" viewBox="0 0 160 10" aria-hidden="true"><path d="M0 5 Q80 0 160 5 L160 10 L0 10Z" fill="#7cb342"/></svg>
</section>

<!-- ROW 2 -->
<section class="piece front" style="left:12px;top:286px">
  <div class="photo house" role="img" aria-label="Photo of a Marlow home exterior"></div>
  <div class="brand"><span class="dot"></span>FindMarlowHomesteads</div>
  <svg class="swoosh" width="192" height="30" viewBox="0 0 192 30" aria-hidden="true"><path d="M0 22 Q70 2 192 14 L192 30 L0 30Z" fill="#7cb342" opacity=".35"/></svg>
  <div class="photo agent" role="img" aria-label="Portrait of the listing agent"></div>
  <p class="search">SEARCH</p>
  <p class="hundreds">HUNDREDS</p>
  <p class="partner"><i></i>Harlan Realty</p>
  <p class="teaser">A new foreclosure listing in your area will be listed soon!</p>
  <p class="footer">Join FindMarlowHomesteads.example to learn more.</p>
</section>

<section class="piece back" style="left:211px;top:286px">
  <div class="brand"><span class="dot"></span>FindMarlowHomesteads</div>
  <div class="stamp"></div>
  <div class="photo listing-main" role="img" aria-label="Main listing photo"></div>
  <div class="photo listing-a" role="img" aria-label="Listing interior photo"></div>
  <div class="photo listing-b" role="img" aria-label="Listing yard photo"></div>
  <p class="mailing">Resident Name<br>12 Harbor Lane<br>Marlow, SC 29400</p>
  <p class="headline">DON'T MISS THIS<br><b>OPPORTUNITY!</b></p>
  <div class="photo agent" role="img" aria-label="Agent portrait"></div>
  <p class="alert">NEW LISTING ALERT – Sign up and receive listings today!</p>
  <p class="disclaimer">We are your Marlow Foreclosure Specialist! This property is NOT listed in MLS yet.</p>
  <div class="icons"><i></i><i></i><i></i></div>
  <p class="site">www.FindMarlowHomesteads.example</p>
  <svg class="wave" width="274" height="40" viewBox="0 0 274 40" aria-hidden="true"><path d="M0 26 Q120 6 274 24 L274 40 L0 40Z" fill="#7cb342"/><path d="M0 32 Q140 16 274 32 L274 40 L0 40Z" fill="#1b4f8f"/></svg>
</section>

<span class="piece-label" style="left:752px;top:290px">Business Card Front</span>
<section class="piece bcard" style="left:749px;top:307px">
  <div class="brand"><span class="dot"></span>FindMarlow</div>
  <p class="details"><strong>Agent Name</strong><br>Foreclosure Specialist<br>555-0142</p>
  <svg class="wave" width="115" height="20" viewBox="0 0 115 20" aria-hidden="true"><path d="M0 11 Q58 0 115 9 L115 20 L0 20Z" fill="#1b4f8f"/><path d="M0 15 Q58 7 115 14 L115 20 L0 20Z" fill="#7cb342"/></svg>
</section>

<span class="piece-label" style="left:850px;top:395px">Business Card Back</span>
<section class="piece bcard-back green" style="left:845px;top:413px">
  <div class="brand"><span class="dot"></span>FindMarlow</div>
</section>

<span class="piece-label" style="left:1020px;top:356px">Email Signature</span>
<section class="piece signature" style="left:1003px;top:373px">
  <div class="brand"><span class="dot"></span>FindMarlow</div>
  <p class="details"><strong>Agent Name</strong><br>Foreclosure Specialist<br>555-0142</p>
  <svg class="wave" width="160" height="10" viewBox="0 0 160 10" aria-hidden="true"><path d="M0 5 Q80 0 160 5 L160 10 L0 10Z" fill="#1b4f8f"/></svg>
</section>

</body>
</html>
```